labels loose leaf tea business

I am in need of a label redo! I have attatched a couple of our old logo labels (still currently using these labels) also i have our new logo that we have loaded on the website feel free to look. www.brewvanto.com i bought the business a year ago and have been wanting to get a new look for a minimal cost.we use the labels that are 4' by 3 1/3' on the bags that hold 100 grams the bag is 5.25"x 8 "stand up pouch and the smaller bag which is 4.25x 6.75" we have used a 2x2 label (which doesn't have room for as much detail. the bags are a matte silver at the time.
i am considering going to either a matte white or there is an aqua co lour not sure if that would work or there is a nice white or silver grey rice paper looking bag i am getting prices.
i would consider a larger label format on this bag as well for retail i need my logo the address and the telephone and website all the ingredients as well as tea type and caffiene content i like to include a short description of the tea, as well as country of origin could be fun.. i have included the steep time and possibly this is something to take into consideration is to make a small info graphic of the steep times that is the same sticker to go on the reverse side of each bag the same.could include the address and website... as you can see my bags have had a different color banner per the type of tea Which my customers are used to that idea pink means fruit black is abrown label blue is herbal etc.
to say what is my style is kind of hard for me i included the two pieces of art work from bright harbour ...the coffee label i liked the bottom part simple and straight forward, (i could also look into seeing how much it would cost to heat stamp my logo on each bag) the second one i do kind of like had drawn also sort of vintage the new logo being aqua and grey to me is fresh and light....really i don't like busy or fussy or Victorian i like a bit unusual ( like the sticker on the kraft paper bag! but it could be a pain to put on straight every time i think the one on the biscotti (art image 3) is kind of neat how its applied the other way...
Anyway my market is some retail/ farmers markets etc.. and website.as well as our own retail shop.we have about 90 kinds of tea so i need to be able to edit and print these myself as to hold stock on labels is not cost effective.
i also should say we use the 4 oz metal tins which i use the same labels size as the large bag but mayb we could design it to fit around the whole tin.
well i hope this is enough info for you and i am super excited to see the products you come up with

Project Deadline Extended Reason: Thank you for taking time to look at my design project. i feel to extend the time as i have never done this before and realize some of you may have better ideas then i have and i feel like you may need more time as well and i have also been talking to some product manufacturers such as the pouches and printer and label makers, i think if possible i will head in the direction of getting a stock label printed where the basic information is pre-printed and i can just change the product detail AS needed.This however may throw a different twist on the labels as i'm not sure that the colored banner such as i had is the way to go.i can see potential in a couple of the designs.However much i wish i could get my logo preprinted ont he bags its not an option at this point its too pricy...so yay keep the designs coming we aren't finished yet! Added Sunday, February 12, 2017

Project Deadline Extended Reason: i am giving five more days, my reason being i have been ill and dont feel like i have the energy to give my full attention too the project as well as we have a wedding on the weekend...i see some close competiton here....and am getting excited as well as nervous as how i will really pick between so many cool designs Added Thursday, February 16, 2017

Project Deadline Extended
Reason: one more deadline... giving some of you designers a chance to get them in that had started on the designs please know this is the last extension and i am not super super excited about any of them yet.....i am looking for a label that can be changed up for the different tea types such as Tomsk provided so far.... so let your imaginations go and become creative, thanks for all the awesome effort so far.....

Target Market(s)

website,farmers markets, retail...seems to cover a broad spectrum of ages

Industry/Entity Type

Business

Colors
86cfc6

Requirements
Must have
• Brewvanto is the name
• www.brewvanto.com website
• packaged and blended in Canada
• Hollis Alberta
• 403-718-2590
• 100 grams or 50 grams
• Tea type and name
• the steeping time and water temp and amount of tea
Nice to have
• Discover Loose leaf tea at its purest i s on the logo
• wouldn't have to have it there could take off and put somewhere else
• description of the tea as seen on the old tea labels i would like included

```html
<!DOCTYPE html>
<html lang="en">
<head>
<meta charset="utf-8">
<title>Brewvanto Tea Labels</title>
<link rel="stylesheet" href="https://fonts.googleapis.com/css2?family=Josefin+Sans:wght@300;400&family=Arimo:wght@400&display=swap">
<style>
  :root {
    --backdrop: #e6e4e1;
    --label-paper: #ffffff;
    --brand-mint: #7fcfc1;
    --brand-grey: #b9b9b9;
    --ink: #2b2b2b;
    --mint-band: #9fdcc6;
    --mint-pattern-a: #2a8f7e;
    --mint-pattern-b: #4a4f8c;
    --mint-rule: #3e8e84;
    --mint-dots: #4a4f8c;
    --purple-band: #9c6fd0;
    --purple-pattern-a: #8d5cc7;
    --purple-pattern-b: #f1eaf8;
    --crimson-band: #b8234e;
    --crimson-pattern-a: #e8913f;
    --crimson-pattern-b: #c42a5a;
    --yellow-band: #ece57c;
    --yellow-pattern-a: #f3d66a;
    --yellow-pattern-b: #f3b69a;
  }

  * { box-sizing: border-box; margin: 0; padding: 0; }

  html, body {
    width: 1200px;
    height: 454px;
    overflow: hidden;
    background: var(--backdrop);
  }

  .label-range {
    position: relative;
    width: 1200px;
    height: 454px;
  }

  .label {
    position: absolute;
    width: 216px;
    height: 400px;
    background: var(--label-paper);
    display: flex;
    flex-direction: column;
    align-items: center;
    overflow: hidden;
    transform-origin: top left;
    --pattern-height: 152px;
  }

  .label--small {
    height: 432px;
    transform: scale(0.607);
    --pattern-height: 178px;
  }

  .label--strawberry { left: 38px; top: 0; }
  .label--butterscotch { left: 436px; top: 52px; }
  .label--cucumber-crimson { left: 706px; top: 52px; }
  .label--cucumber-yellow { left: 976px; top: 52px; }

  .label__pattern {
    width: 100%;
    height: var(--pattern-height);
    flex: none;
  }

  .label--strawberry .label__pattern {
    background: linear-gradient(135deg, var(--mint-pattern-a) 0%, #e9f3f1 45%, var(--mint-pattern-b) 100%);
    opacity: 0.55;
  }
  .label--butterscotch .label__pattern {
    background: linear-gradient(135deg, var(--purple-pattern-a) 0%, var(--purple-pattern-b) 50%, var(--purple-pattern-a) 100%);
    opacity: 0.7;
  }
  .label--cucumber-crimson .label__pattern {
    background: linear-gradient(135deg, var(--crimson-pattern-a) 0%, #fbe9dc 45%, var(--crimson-pattern-b) 100%);
    opacity: 0.75;
  }
  .label--cucumber-yellow .label__pattern {
    background: linear-gradient(135deg, var(--yellow-pattern-a) 0%, #fff8e4 50%, var(--yellow-pattern-b) 100%);
    opacity: 0.8;
  }

  .brand {
    margin-top: 24px;
    display: flex;
    align-items: center;
    gap: 6px;
    height: 32px;
  }

  .brand__dot {
    width: 9px;
    height: 9px;
    border-radius: 50%;
    background: var(--brand-grey);
  }

  .brand__name {
    font-family: "Josefin Sans", sans-serif;
    font-weight: 300;
    font-size: 27px;
    color: var(--brand-mint);
    line-height: 1;
  }

  .brand__tagline {
    margin-top: 2px;
    font-family: "Josefin Sans", sans-serif;
    font-weight: 300;
    font-size: 6.5px;
    letter-spacing: 0.3px;
    text-transform: uppercase;
    color: var(--brand-mint);
  }

  .tea-band {
    margin-top: 14px;
    width: 100%;
    height: 31px;
    display: flex;
    flex-direction: column;
    align-items: center;
    justify-content: center;
    color: #ffffff;
    flex: none;
  }

  .label--strawberry .tea-band { background: var(--mint-band); }
  .label--butterscotch .tea-band { background: var(--purple-band); }
  .label--cucumber-crimson .tea-band { background: var(--crimson-band); }
  .label--cucumber-yellow .tea-band { background: var(--yellow-band); }

  .tea-band__name {
    font-family: "Josefin Sans", sans-serif;
    font-weight: 400;
    font-size: 15px;
    font-variant: small-caps;
    letter-spacing: 0.6px;
    line-height: 1;
  }

  .tea-band__type {
    margin-top: 2px;
    font-family: "Arimo", sans-serif;
    font-size: 5.5px;
    text-transform: uppercase;
    letter-spacing: 0.2px;
  }

  .tea-description {
    margin-top: 28px;
    padding: 0 18px;
    font-family: "Arimo", sans-serif;
    font-size: 9.5px;
    line-height: 1.2;
    text-align: center;
    color: var(--ink);
  }

  .dot-row {
    margin-top: 6px;
    display: flex;
    gap: 20px;
    font-size: 5px;
    letter-spacing: 2.5px;
    line-height: 1;
  }

  .label--strawberry .dot-row { color: var(--mint-dots); }
  .label--butterscotch .dot-row { color: var(--purple-band); }
  .label--cucumber-crimson .dot-row { color: var(--crimson-pattern-a); }
  .label--cucumber-yellow .dot-row { color: var(--yellow-pattern-b); }

  .origin-line {
    margin-top: 3px;
    width: 100%;
    padding: 3px 0;
    border-top: 0.8px solid var(--rule-colour, var(--mint-rule));
    border-bottom: 0.8px solid var(--rule-colour, var(--mint-rule));
    font-family: "Arimo", sans-serif;
    font-size: 6.5px;
    text-transform: uppercase;
    text-align: center;
    color: var(--ink);
  }

  .label--butterscotch { --rule-colour: var(--purple-band); }
  .label--cucumber-crimson { --rule-colour: var(--crimson-band); }
  .label--cucumber-yellow { --rule-colour: var(--yellow-band); }

  .ingredients {
    margin-top: 6px;
    padding: 0 8px;
    align-self: stretch;
    font-family: "Arimo", sans-serif;
    font-size: 5.2px;
    line-height: 1.35;
    text-transform: uppercase;
    color: var(--ink);
  }

  .ingredients__heading { font-variant: small-caps; }
</style>
</head>
<body>
<main class="label-range">

  <article class="label label--strawberry">
    <div class="label__pattern" role="img" aria-label="Decorative quatrefoil lattice pattern in teal and navy"></div>
    <div class="brand"><span class="brand__dot"></span><span class="brand__name">Brewvanto</span></div>
    <p class="brand__tagline">Discover loose leaf tea at its purest</p>
    <div class="tea-band">
      <h2 class="tea-band__name">Strawberry Mist</h2>
      <p class="tea-band__type">Caffeine free loose / fruit tea</p>
    </div>
    <p class="tea-description">Sweet sugary notes of butterscotch blend in perfect harmony with the decadent characteristics of pu-erh.</p>
    <div class="dot-row"><span>◆◆◆◆◆◆</span><span>◆◆◆◆◆◆</span></div>
    <p class="origin-line">Packaged and blended in Canada</p>
    <p class="ingredients"><span class="ingredients__heading">Ingredients:</span> luxury natural dried apple pieces, hibiscus, rosehip natural dried orange, calendula petals, natural flavors.</p>
  </article>

  <article class="label label--small label--butterscotch">
    <div class="label__pattern" role="img" aria-label="Decorative woven diamond pattern in purple"></div>
    <div class="brand"><span class="brand__dot"></span><span class="brand__name">Brewvanto</span></div>
    <p class="brand__tagline">Discover loose leaf tea at its purest</p>
    <div class="tea-band">
      <h2 class="tea-band__name">Butterscotch Dessert</h2>
      <p class="tea-band__type">Caffeine free loose / fruit tea</p>
    </div>
    <p class="tea-description">Sweet sugary notes of butterscotch blend in perfect harmony with the decadent characteristics of pu-erh.</p>
    <div class="dot-row"><span>◆◆◆◆◆◆</span><span>◆◆◆◆◆◆</span></div>
    <p class="origin-line">Packaged and blended in Canada</p>
    <p class="ingredients"><span class="ingredients__heading">Ingredients:</span> luxury natural dried apple pieces, hibiscus, rosehip natural dried orange, calendula petals, natural flavors.</p>
  </article>

  <article class="label label--small label--cucumber-crimson">
    <div class="label__pattern" role="img" aria-label="Decorative star and lattice pattern in orange and crimson"></div>
    <div class="brand"><span class="brand__dot"></span><span class="brand__name">Brewvanto</span></div>
    <p class="brand__tagline">Discover loose leaf tea at its purest</p>
    <div class="tea-band">
      <h2 class="tea-band__name">Cucumber Melon</h2>
      <p class="tea-band__type">Caffeine free loose / fruit tea</p>
    </div>
    <p class="tea-description">Sweet sugary notes of butterscotch blend in perfect harmony with the decadent characteristics of pu-erh.</p>
    <div class="dot-row"><span>★★★★★★</span><span>★★★★★★</span></div>
    <p class="origin-line">Packaged and blended in Canada</p>
    <p class="ingredients"><span class="ingredients__heading">Ingredients:</span> luxury natural dried apple pieces, hibiscus, rosehip natural dried orange, calendula petals, natural flavors.</p>
  </article>

  <article class="label label--small label--cucumber-yellow">
    <div class="label__pattern" role="img" aria-label="Decorative circle and diamond pattern in yellow and peach"></div>
    <div class="brand"><span class="brand__dot"></span><span class="brand__name">Brewvanto</span></div>
    <p class="brand__tagline">Discover loose leaf tea at its purest</p>
    <div class="tea-band">
      <h2 class="tea-band__name">Cucumber Melon</h2>
      <p class="tea-band__type">Caffeine free loose / fruit tea</p>
    </div>
    <p class="tea-description">Sweet sugary notes of butterscotch blend in perfect harmony with the decadent characteristics of pu-erh.</p>
    <div class="dot-row"><span>★★★★★★</span><span>★★★★★★</span></div>
    <p class="origin-line">Packaged and blended in Canada</p>
    <p class="ingredients"><span class="ingredients__heading">Ingredients:</span> luxury natural dried apple pieces, hibiscus, rosehip natural dried orange, calendula petals, natural flavors.</p>
  </article>

</main>
</body>
</html>
```